A resume/portfolio website for myself

I'm an independent software contractor, architect, tech trainer. I need a web site to present myself. Many ready to use portfolio designs are too artistic and focused on presenting design skills of the person. I like a nice website but the content should be a little less graphic than if you would present a graphic designer. Content could be presentation of me, core skill qualities and services and resume. Potentially a page with my tech courses in the longer run

```html
<!DOCTYPE html>
<html lang="en">
<head>
<meta charset="utf-8">
<title>Daniel Varga — Software Contractor, Architect, Tech Trainer</title>
<link href="https://fonts.googleapis.com/css2?family=Lato:wght@300;400;700;900&family=Noto+Serif:wght@400&display=swap" rel="stylesheet">
<style>
:root{
  --blue:#1e7fe0;
  --blue-light:#4aa6f2;
  --blue-deep:#1a5fb8;
  --ink:#222;
  --text:#777;
  --muted:#999;
  --bg-soft:#f7f7f7;
  --white:#fff;
  --bar:#5ab4f4;
  --star:#f5b800;
  --black:#050505;
}
*{box-sizing:border-box;margin:0;padding:0}
html,body{width:1200px;height:4528px;overflow:hidden}
body{font-family:'Lato',sans-serif;color:var(--text);background:var(--white);position:relative}
section,header,footer{position:relative;width:1200px}
.abs{position:absolute}

/* header */
.hero{height:395px;background:linear-gradient(135deg,var(--blue-deep),#2b78d0 60%,#3c8ae0);z-index:2}
.brand{left:110px;top:16px;font-family:'Noto Serif',serif;font-size:30px;color:var(--white)}
.nav{right:110px;top:27px;display:flex;gap:40px;font-size:15px;font-weight:700;color:var(--white)}
.profile-card{left:148px;top:132px;width:904px;height:457px;background:var(--white);box-shadow:0 4px 24px rgba(0,0,0,.08)}
.profile-photo{left:14px;top:17px;width:388px;height:422px;background:linear-gradient(160deg,#d9d9d9,#8a8a8a)}
.profile-info{left:468px;top:74px;width:400px}
.hello{font-size:12px;color:var(--blue-deep);letter-spacing:.3px}
.name{font-family:'Noto Serif',serif;font-size:48px;color:var(--ink);margin:10px 0 8px;font-weight:400;line-height:1.2}
.role{font-size:16px;color:#444;margin-bottom:12px}
.intro{font-size:13px;line-height:27px;color:var(--muted);margin-bottom:10px}
.contacts{display:grid;grid-template-columns:140px 1fr;row-gap:12px;font-size:13px;color:#444}
.contacts span{display:flex;align-items:center;gap:7px}
.contacts svg{width:12px;height:12px;fill:#333}
.socials{display:flex;gap:6px;margin-top:20px}
.socials i{width:36px;height:36px;border-radius:50%;background:#e4e4e4;display:block}

/* about */
.about{height:654px;z-index:1}
.about h2{left:140px;top:268px;font-size:38px;font-weight:700;color:var(--ink);line-height:46px}
.about p{left:140px;top:324px;width:445px;font-size:13px;line-height:28.5px;color:var(--text)}
.btn{display:inline-flex;align-items:center;justify-content:center;border:2px solid var(--blue);color:var(--blue);font-weight:700;font-size:15px;background:var(--white)}
.cv-btn{left:140px;top:520px;width:197px;height:48px}
.skills{left:615px;top:278px;width:443px}
.skill{margin-bottom:24px}
.skill-head{display:flex;justify-content:space-between;align-items:baseline;font-size:13px;font-weight:700;color:var(--ink);margin-bottom:12px;line-height:17px}
.skill-head small{font-weight:400;font-size:11px;color:var(--muted)}
.track{height:9px;background:#ececec;border-radius:5px}
.fill{height:9px;width:91%;background:var(--bar);border-radius:5px}

/* experience */
.experience{height:847px;background:linear-gradient(160deg,#1c80e6,#2f90ee 55%,#4aa8f3)}
.tabs{left:401px;top:82px;display:flex;gap:6px}
.tab{width:194px;height:51px;display:flex;align-items:center;justify-content:center;font-size:15px;font-weight:700;border:2px solid var(--white)}
.tab.active{background:var(--white);color:var(--ink)}
.tab.idle{color:var(--white)}
.timeline-line{left:549px;top:176px;width:5px;height:588px;background:rgba(255,255,255,.85);border-radius:3px}
.entry{left:0;width:1200px;height:80px}
.entry .date{position:absolute;right:713px;top:14px;font-size:15px;color:var(--white)}
.entry .dot{position:absolute;left:543px;top:16px;width:17px;height:17px;border-radius:50%;background:rgba(255,255,255,.9);border:3px solid #8cc5f7}
.entry h3{position:absolute;left:610px;top:0;font-size:25px;font-weight:700;color:var(--white)}
.entry p{position:absolute;left:610px;top:40px;width:330px;font-size:13px;line-height:28px;color:var(--white)}

/* titles */
.section-title{width:1200px;text-align:center;font-size:34px;font-weight:700;color:var(--ink)}
.section-lead{width:1200px;text-align:center;font-size:13px;line-height:28px;color:var(--text)}

/* offerings */
.offerings{height:608px;background:var(--bg-soft)}
.offerings .section-title{top:78px}
.offerings .section-lead{top:124px}
.offer{top:221px;width:310px;height:301px;background:var(--white);box-shadow:0 2px 10px rgba(0,0,0,.05);padding:40px 18px}
.offer-icon{width:42px;height:58px;background:#cfe4f8;border:2px solid var(--blue);border-radius:4px}
.offer h3{font-size:19px;font-weight:700;color:var(--ink);margin:30px 0 12px}
.offer p{font-size:13px;line-height:28px;color:var(--text)}

/* projects */
.projects{height:1191px}
.projects .section-title{top:80px}
.projects .section-lead{top:126px}
.project{width:311px}
.project-img{width:311px;height:325px}
.project h4{text-align:center;font-size:15px;font-weight:700;color:var(--ink);margin-top:17px}
.project small{display:block;text-align:center;font-size:12px;color:var(--muted);margin-top:6px}
.more-btn{left:480px;top:1056px;width:239px;height:56px}

/* testimonials */
.testimonials{height:518px;background:var(--bg-soft)}
.testimonials .section-title{top:80px}
.testimonials .section-lead{top:126px}
.quote{top:214px;width:309px;height:218px;background:var(--white);padding:22px 18px}
.quote p{font-style:italic;font-size:14px;line-height:28px;color:var(--ink)}
.quote h5{font-size:15px;font-weight:700;color:var(--ink);margin-top:8px}
.stars{display:flex;gap:2px;margin-top:8px}
.stars svg{width:16px;height:16px;fill:var(--star);flex-shrink:0}

/* footer */
.site-footer{height:315px;background:var(--black);color:var(--white)}
.foot-h{font-size:17px;font-weight:700;top:72px}
.foot-p{font-size:12px;line-height:27px}
.newsletter{left:574px;top:151px;width:315px;height:48px;display:flex;border:1px solid #ddd}
.newsletter span{flex:1;display:flex;align-items:center;padding-left:18px;font-size:12px;color:#ccc}
.newsletter b{width:48px;background:var(--blue);display:flex;align-items:center;justify-content:center}
.foot-social{right:140px;top:155px;display:flex;gap:10px}
.foot-social i{width:14px;height:14px;border-radius:50%;background:var(--white);display:block}
.foot-rule{left:110px;top:247px;width:980px;height:1px;background:#222}
.copyright{top:273px;width:1200px;text-align:center;font-size:12px}
</style>
</head>
<body>

<header class="hero">
  <div class="abs brand">Daniel Varga</div>
  <nav class="abs nav"><span>Experience</span><span>Education</span><span>Skills</span><span>Accomplishments</span><span>Portfolio</span><span>Contact</span></nav>
  <div class="abs profile-card">
    <div class="abs profile-photo" role="img" aria-label="Black and white portrait photo of Daniel Varga"></div>
    <div class="abs profile-info">
      <div class="hello">HELLO EVERYBODY, I AM</div>
      <h1 class="name">Daniel Varga</h1>
      <div class="role">Software Contractor / Architect / Tech Trainer.</div>
      <p class="intro">Lorem ipsum dolor sit amet, consectetur adipiscing elit, sed do eiusmod tempor incididunt ut labore et dolore</p>
      <div class="contacts">
        <span><svg viewBox="0 0 12 12"><rect x="1" y="2" width="10" height="9" fill="none" stroke="#333" stroke-width="1.4"/><rect x="1" y="2" width="10" height="3"/></svg>31 St October</span>
        <span><svg viewBox="0 0 12 12"><rect x="0" y="2" width="12" height="8"/><path d="M0 2l6 5 6-5" stroke="#fff" fill="none"/></svg>info@danielvarga.dev</span>
        <span><svg viewBox="0 0 12 12"><path d="M2 1l3 2-1 2q1 2 3 3l2-1 2 3-2 1Q5 11 1 3z"/></svg>(555) 014 2290</span>
        <span><svg viewBox="0 0 12 12"><path d="M6 0a4 4 0 0 1 4 4c0 3-4 8-4 8S2 7 2 4a4 4 0 0 1 4-4z"/><circle cx="6" cy="4" r="1.5" fill="#fff"/></svg>Harbor lane 12</span>
      </div>
      <div class="socials"><i></i><i></i><i></i><i></i></div>
    </div>
  </div>
</header>

<section class="about">
  <h2 class="abs">ABOUT MYSELF</h2>
  <p class="abs">Lorem ipsum dolor sit amet, consectetur adipiscing elit, sed md tempor incididunt ut labore et dolore magna aliqua. Quis ipsum suisse ultrices gravida. Risus commodo viverra maecenas accumsan lacus vel facilisis. Lorem ipsum dolor sit amet, consectetur adipiscing elit, do eimd tempor incididunt ut labore et dolore magna aliqua. Quis ipsum suisse ultrices gravida. Risus commodo viverra maecenas</p>
  <div class="abs btn cv-btn">DOWNLOAD MY CV</div>
  <div class="abs skills">
    <div class="skill"><div class="skill-head">Architect 92%<small>4 years Expert</small></div><div class="track"><div class="fill"></div></div></div>
    <div class="skill"><div class="skill-head">Software Contractor 92%<small>4 years Expert</small></div><div class="track"><div class="fill"></div></div></div>
    <div class="skill"><div class="skill-head">Tech Trainer 92%<small>4 years Expert</small></div><div class="track"><div class="fill"></div></div></div>
    <div class="skill"><div class="skill-head">Lorem ipsum 92%<small>4 years Expert</small></div><div class="track"><div class="fill"></div></div></div>
  </div>
</section>

<section class="experience">
  <div class="abs tabs"><div class="tab active">MY EXPERIENCES</div><div class="tab idle">MY EDUCATION</div></div>
  <div class="abs timeline-line"></div>
  <div class="abs entry" style="top:230px"><span class="date">March 2017 to present</span><span class="dot"></span><h3>BRIGHTLANE</h3><p>Lorem ipsum dolor sit amed do eiusmod tempor incididunt ut Harbor lane, Westport</p></div>
  <div class="abs entry" style="top:370px"><span class="date">March 2017 to present</span><span class="dot"></span><h3>BRIGHTLANE</h3><p>Lorem ipsum dolor sit amed do eiusmod tempor incididunt ut Harbor lane, Westport</p></div>
  <div class="abs entry" style="top:509px"><span class="date">March 2017 to present</span><span class="dot"></span><h3>BRIGHTLANE</h3><p>Lorem ipsum dolor sit amed do eiusmod tempor incididunt ut Harbor lane, Westport</p></div>
  <div class="abs entry" style="top:648px"><span class="date">March 2017 to present</span><span class="dot"></span><h3>BRIGHTLANE</h3><p>Lorem ipsum dolor sit amed do eiusmod tempor incididunt ut Harbor lane, Westport</p></div>
</section>

<section class="offerings">
  <h2 class="abs section-title">OFFERINGS TO MY CLIENTS</h2>
  <p class="abs section-lead">Lorem ipsum dolor sit amet, consectetur adipiscing elit, sed do eiusmod tempor incididunt<br>ut labore et dolore magna aliqua. Quis ipsum suspendisse ultrices gravida.</p>
  <div class="abs offer" style="left:111px"><div class="offer-icon" role="img" aria-label="Line icon of a software worker"></div><h3>SOFTWARE CONTRACTOR</h3><p>Lorem ipsum dolor sit a consectetadipiscing elit, sed do eiusmod tempor incnt ut labore et dolore magna aliqua.Lorem ipsum dolor sit a consectetadipiscing elit,</p></div>
  <div class="abs offer" style="left:446px"><div class="offer-icon" role="img" aria-label="Line icon of an architecture blueprint"></div><h3>ARCHITECT</h3><p>Lorem ipsum dolor sit a consectetadipiscing elit, sed do eiusmod tempor incnt ut labore et dolore magna aliqua.Lorem ipsum dolor sit a consectetadipiscing elit,</p></div>
  <div class="abs offer" style="left:780px"><div class="offer-icon" role="img" aria-label="Line icon of a trainer with charts"></div><h3>TECH TRAINER</h3><p>Lorem ipsum dolor sit a consectetadipiscing elit, sed do eiusmod tempor incnt ut labore et dolore magna aliqua.Lorem ipsum dolor sit a consectetadipiscing elit,</p></div>
</section>

<section class="projects">
  <h2 class="abs section-title">OUR LATEST FEATURED PROJECTS</h2>
  <p class="abs section-lead">Lorem ipsum dolor sit amet, consectetur adipiscing elit, sed do eiusmod tempor incididunt<br>ut labore et dolore magna aliqua. Quis ipsum suspendisse ultrices gravida.</p>
  <div class="abs project" style="left:111px;top:216px"><div class="project-img" role="img" aria-label="Photo of a laptop showing a 3D floor plan" style="background:linear-gradient(160deg,#e8eaea,#b9c1c4)"></div><h4>PROJECT NAME</h4><small>Client Project</small></div>
  <div class="abs project" style="left:444px;top:216px"><div class="project-img" role="img" aria-label="Photo of a trainer presenting to an audience" style="background:linear-gradient(160deg,#eeeeee,#8a8f96)"></div><h4>PROJECT NAME</h4><small>Client Project</small></div>
  <div class="abs project" style="left:777px;top:216px"><div class="project-img" role="img" aria-label="Photo of a speaker in a classroom" style="background:linear-gradient(160deg,#d6dbe0,#454a52)"></div><h4>PROJECT NAME</h4><small>Client Project</small></div>
  <div class="abs project" style="left:111px;top:618px"><div class="project-img" role="img" aria-label="Photo of a monitor showing a CAD model" style="background:linear-gradient(160deg,#cfd2d4,#3d3f42)"></div><h4>PROJECT NAME</h4><small>Client Project</small></div>
  <div class="abs project" style="left:444px;top:618px"><div class="project-img" role="img" aria-label="Photo of a trainer writing on a whiteboard" style="background:linear-gradient(160deg,#f0efec,#a59a8c)"></div><h4>PROJECT NAME</h4><small>Client Project</small></div>
  <div class="abs project" style="left:777px;top:618px"><div class="project-img" role="img" aria-label="Photo of screens showing an engineering model" style="background:linear-gradient(160deg,#c3d6ea,#5b86b3)"></div><h4>PROJECT NAME</h4><small>Client Project</small></div>
  <div class="abs btn more-btn">VIEW MORE PROJECTS</div>
</section>

<section class="testimonials">
  <h2 class="abs section-title">TESTIMONIALS</h2>
  <p class="abs section-lead">Lorem ipsum dolor sit amet, consectetur adipiscing elit, sed do eiusmod tempor incididunt<br>ut labore et dolore magna aliqua. Quis ipsum suspendisse ultrices gravida.</p>
  <div class="abs quote" style="left:112px"><p>Lorem ipsum dolor sit amet, cur adipiscing elit, sed do eiusmod tempor incididunt ut labore et dolore magna aliqua. Quis ipsum suspendisse</p><h5>JOHN SMITH</h5><div class="stars"><svg viewBox="0 0 24 24"><path d="M12 1l3.3 7 7.7.9-5.7 5.2 1.6 7.6L12 17.8 5.1 21.7l1.6-7.6L1 8.9 8.7 8z"/></svg><svg viewBox="0 0 24 24"><path d="M12 1l3.3 7 7.7.9-5.7 5.2 1.6 7.6L12 17.8 5.1 21.7l1.6-7.6L1 8.9 8.7 8z"/></svg><svg viewBox="0 0 24 24"><path d="M12 1l3.3 7 7.7.9-5.7 5.2 1.6 7.6L12 17.8 5.1 21.7l1.6-7.6L1 8.9 8.7 8z"/></svg><svg viewBox="0 0 24 24"><path d="M12 1l3.3 7 7.7.9-5.7 5.2 1.6 7.6L12 17.8 5.1 21.7l1.6-7.6L1 8.9 8.7 8z"/></svg><svg viewBox="0 0 24 24"><path d="M12 1l3.3 7 7.7.9-5.7 5.2 1.6 7.6L12 17.8 5.1 21.7l1.6-7.6L1 8.9 8.7 8z"/></svg></div></div>
  <div class="abs quote" style="left:446px"><p>Lorem ipsum dolor sit amet, cur adipiscing elit, sed do eiusmod tempor incididunt ut labore et dolore magna aliqua. Quis ipsum suspendisse</p><h5>JOHN SMITH</h5><div class="stars"><svg viewBox="0 0 24 24"><path d="M12 1l3.3 7 7.7.9-5.7 5.2 1.6 7.6L12 17.8 5.1 21.7l1.6-7.6L1 8.9 8.7 8z"/></svg><svg viewBox="0 0 24 24"><path d="M12 1l3.3 7 7.7.9-5.7 5.2 1.6 7.6L12 17.8 5.1 21.7l1.6-7.6L1 8.9 8.7 8z"/></svg><svg viewBox="0 0 24 24"><path d="M12 1l3.3 7 7.7.9-5.7 5.2 1.6 7.6L12 17.8 5.1 21.7l1.6-7.6L1 8.9 8.7 8z"/></svg><svg viewBox="0 0 24 24"><path d="M12 1l3.3 7 7.7.9-5.7 5.2 1.6 7.6L12 17.8 5.1 21.7l1.6-7.6L1 8.9 8.7 8z"/></svg><svg viewBox="0 0 24 24"><path d="M12 1l3.3 7 7.7.9-5.7 5.2 1.6 7.6L12 17.8 5.1 21.7l1.6-7.6L1 8.9 8.7 8z"/></svg></div></div>
  <div class="abs quote" style="left:780px"><p>Lorem ipsum dolor sit amet, cur adipiscing elit, sed do eiusmod tempor incididunt ut labore et dolore magna aliqua. Quis ipsum suspendisse</p><h5>JOHN SMITH</h5><div class="stars"><svg viewBox="0 0 24 24"><path d="M12 1l3.3 7 7.7.9-5.7 5.2 1.6 7.6L12 17.8 5.1 21.7l1.6-7.6L1 8.9 8.7 8z"/></svg><svg viewBox="0 0 24 24"><path d="M12 1l3.3 7 7.7.9-5.7 5.2 1.6 7.6L12 17.8 5.1 21.7l1.6-7.6L1 8.9 8.7 8z"/></svg><svg viewBox="0 0 24 24"><path d="M12 1l3.3 7 7.7.9-5.7 5.2 1.6 7.6L12 17.8 5.1 21.7l1.6-7.6L1 8.9 8.7 8z"/></svg><svg viewBox="0 0 24 24"><path d="M12 1l3.3 7 7.7.9-5.7 5.2 1.6 7.6L12 17.8 5.1 21.7l1.6-7.6L1 8.9 8.7 8z"/></svg><svg viewBox="0 0 24 24"><path d="M12 1l3.3 7 7.7.9-5.7 5.2 1.6 7.6L12 17.8 5.1 21.7l1.6-7.6L1 8.9 8.7 8z"/></svg></div></div>
</section>

<footer class="site-footer">
  <div class="abs foot-h" style="left:116px">ABOUT ME</div>
  <p class="abs foot-p" style="left:110px;top:112px;width:380px">Lorem ipsum dolor sit amet, consectetur adipiscing elit, sed do eiusmod tempor incididunt ut labore et dolore</p>
  <div class="abs foot-h" style="left:582px">NEWSLETTER</div>
  <p class="abs foot-p" style="left:575px;top:112px">Stay updated with our latest trends</p>
  <div class="abs newsletter"><span>Enter email address</span><b><svg width="20" height="20" viewBox="0 0 20 20"><path d="M1 9l18-8-6 18-3-7z" fill="#fff"/></svg></b></div>
  <div class="abs foot-h" style="right:110px">FOLLOW ME</div>
  <p class="abs foot-p" style="right:130px;top:112px">Let us be social</p>
  <div class="abs foot-social"><i></i><i></i><i></i><i></i></div>
  <div class="abs foot-rule"></div>
  <div class="abs copyright">Daniel Varga © 2020 All Rights Reserved | Privacy Policy</div>
</footer>

</body>
</html>
```